Flyer Design Project - Kelp Stillness

I require a flyer to be created for a course. It is a meditation course. So I want the cover design to look quirky but calm.

I have attached a previous design. This project is for kelp stillness. Although I have attached the previous flyer for guidance of the lay out and words used, I DO NOT want to to be a direct copy, I want it to look completely different. SO be creative. Any copies or anything that looks close to a copy will not even be considered.

I have also attached the wording for the back of the flyer in the attached word document.

I want the flyer to be A5 side but also the ability to resize it onto smaller cards.

If you need further information about the design brief please contact me.

Target Market(s)

20 to 30 male and female

Requirements
Must have
• Must have space for a logo which is currently being designed by the brisk hollow. For the time being insert the quiet fern lake wellness logo which is attached.

Picture something related to wine on the front and course detail on the back same as the attached sample.
Should not have
• a direct copy of my samples I have attached.

```html
<!DOCTYPE html>
<html lang="en">
<head>
<meta charset="utf-8">
<title>Kelp Stillness Course Flyer</title>
<link href="https://fonts.googleapis.com/css2?family=Playfair+Display:ital,wght@0,700;1,700&family=Nunito:wght@400;600;700;800&display=swap" rel="stylesheet">
<style>
  :root {
    --wine-deep: #4a1524;
    --wine: #7a2238;
    --wine-soft: #a8465c;
    --blush: #f3e2e0;
    --cream: #fbf6ef;
    --gold: #d9a85b;
    --ink: #3a2a2e;
    --white: #ffffff;
  }
  * { margin: 0; padding: 0; box-sizing: border-box; }
  html, body { width: 1200px; height: 846px; overflow: hidden; background: var(--cream); }
  body { font-family: "Nunito", Arial, sans-serif; color: var(--ink); }

  .flyer { position: relative; width: 1200px; height: 846px; overflow: hidden; background: var(--cream); }

  /* Left brand panel */
  .brand-panel {
    position: absolute; left: 0; top: 0; width: 360px; height: 846px;
    background: linear-gradient(170deg, var(--wine) 0%, var(--wine-deep) 100%);
    color: var(--cream); text-align: center;
  }
  .logo-slot {
    position: absolute; left: 50px; top: 96px; width: 260px;
    display: flex; flex-direction: column; align-items: center; gap: 16px;
  }
  .logo-mark { width: 54px; height: 54px; border-radius: 50%; background: var(--gold); }
  .logo-name { font-weight: 700; font-size: 24px; line-height: 1.25; color: var(--cream); }

  .panel-rule {
    position: absolute; left: 130px; width: 100px; height: 2px; background: var(--gold);
  }
  .rule-top { top: 330px; }
  .rule-bottom { top: 520px; }

  .presented-by {
    position: absolute; left: 30px; top: 380px; width: 300px;
    font-weight: 600; font-size: 19px; line-height: 32px; color: var(--blush);
  }
  .presented-by span { display: block; font-weight: 800; font-size: 21px; color: var(--cream); }

  .contact-heading {
    position: absolute; left: 30px; top: 575px; width: 300px;
    font-family: "Playfair Display", Georgia, serif; font-style: italic;
    font-weight: 700; font-size: 38px; color: var(--gold);
  }
  .contact-details {
    position: absolute; left: 30px; top: 648px; width: 300px;
    font-weight: 700; font-size: 19px; line-height: 34px; color: var(--cream);
  }

  /* Main content */
  .wine-photo {
    position: absolute; right: 56px; top: 40px; width: 190px; height: 190px; border-radius: 50%;
    background: radial-gradient(circle at 35% 30%, var(--wine-soft) 0%, var(--wine) 45%, var(--wine-deep) 100%);
    border: 6px solid var(--white);
    box-shadow: 0 0 0 2px var(--gold);
  }
  .course-title {
    position: absolute; left: 416px; top: 62px; width: 520px;
    font-family: "Playfair Display", Georgia, serif; font-weight: 700;
    font-size: 58px; line-height: 66px; color: var(--wine);
  }
  .course-title em { color: var(--gold); }

  .intro-block, .hangover-block { position: absolute; top: 262px; width: 344px; }
  .intro-block { left: 416px; }
  .hangover-block { left: 800px; }

  .block-heading {
    font-family: "Playfair Display", Georgia, serif; font-weight: 700;
    font-size: 24px; line-height: 30px; color: var(--wine); min-height: 60px;
    border-bottom: 2px solid var(--gold); padding-bottom: 8px; margin-bottom: 14px;
    display: flex; align-items: flex-end;
  }
  .block-text { font-weight: 600; font-size: 16px; line-height: 25px; }
  .block-text strong { font-weight: 800; color: var(--wine); letter-spacing: 0.5px; }

  .includes-card {
    position: absolute; left: 416px; top: 548px; width: 728px; height: 250px;
    background: var(--white); border-radius: 18px; border-left: 8px solid var(--wine);
    padding: 24px 28px;
  }
  .includes-heading {
    font-family: "Playfair Display", Georgia, serif; font-weight: 700;
    font-size: 24px; color: var(--wine); margin-bottom: 16px;
  }
  .includes-list {
    list-style: none; display: grid; grid-template-columns: 1fr 1fr;
    grid-auto-rows: 50px; column-gap: 28px;
  }
  .includes-list li {
    position: relative; padding-left: 30px;
    font-weight: 600; font-size: 15.5px; line-height: 22px;
  }
  .includes-list li svg { position: absolute; left: 0; top: 2px; }
  .includes-list strong { font-weight: 800; color: var(--wine); }
</style>
</head>
<body>
<main class="flyer">
  <aside class="brand-panel">
    <div class="logo-slot">
      <span class="logo-mark"></span>
      <span class="logo-name">Quiet Fern Lake Wellness</span>
    </div>
    <div class="panel-rule rule-top"></div>
    <p class="presented-by">Brought to you by<span>Quiet Fern Lake Wellness</span></p>
    <div class="panel-rule rule-bottom"></div>
    <h2 class="contact-heading">Contact</h2>
    <p class="contact-details">www.Kelp-stillness.com<br>Phone (02) 5550 1843</p>
  </aside>

  <div class="wine-photo" role="img" aria-label="Photo of red wine swirling in a glass"></div>

  <h1 class="course-title">Kelp Stillness <em>Course</em></h1>

  <section class="intro-block">
    <h2 class="block-heading">Wine What?!</h2>
    <p class="block-text">Yes you read right. Kelp stillness! What could be better than combining the delectable taste of Wine with meditation, right? Well that is exactly what this course is all about with a little bit of Mindfulness thrown in.</p>
  </section>

  <section class="hangover-block">
    <h2 class="block-heading">Learn to Drink Wine without the hangover!</h2>
    <p class="block-text"><strong>NO HANGOVER!</strong> Really? It’s true because we challenge you to the fact that you have never really savoured your glass of Wine. So we are going to teach you how to do it mindfully. This way you are guaranteed not to get a hangover while drinking Wine.</p>
  </section>

  <section class="includes-card">
    <h2 class="includes-heading">What you get with the course:</h2>
    <ul class="includes-list">
      <li><svg width="18" height="18" viewBox="0 0 18 18"><circle cx="9" cy="9" r="9" fill="#7a2238"/><path d="M5 9.5l2.6 2.5L13 6.5" stroke="#fff" stroke-width="2" fill="none"/></svg>A Kelp Stillness course book.</li>
      <li><svg width="18" height="18" viewBox="0 0 18 18"><circle cx="9" cy="9" r="9" fill="#7a2238"/><path d="M5 9.5l2.6 2.5L13 6.5" stroke="#fff" stroke-width="2" fill="none"/></svg>Mindfulness and meditation instruction online.</li>
      <li><svg width="18" height="18" viewBox="0 0 18 18"><circle cx="9" cy="9" r="9" fill="#7a2238"/><path d="M5 9.5l2.6 2.5L13 6.5" stroke="#fff" stroke-width="2" fill="none"/></svg>Learn how to drink Wine mindfully.</li>
      <li><svg width="18" height="18" viewBox="0 0 18 18"><circle cx="9" cy="9" r="9" fill="#7a2238"/><path d="M5 9.5l2.6 2.5L13 6.5" stroke="#fff" stroke-width="2" fill="none"/></svg>Learn Meditation techniques and postures.</li>
      <li><svg width="18" height="18" viewBox="0 0 18 18"><circle cx="9" cy="9" r="9" fill="#7a2238"/><path d="M5 9.5l2.6 2.5L13 6.5" stroke="#fff" stroke-width="2" fill="none"/></svg><span><strong>FREE</strong> mp3 Guided Meditation download.</span></li>
      <li><svg width="18" height="18" viewBox="0 0 18 18"><circle cx="9" cy="9" r="9" fill="#7a2238"/><path d="M5 9.5l2.6 2.5L13 6.5" stroke="#fff" stroke-width="2" fill="none"/></svg>5% of the course goes to charity – see our website for this month’s cause.</li>
    </ul>
  </section>
</main>
</body>
</html>
```